Business cards - Yoga Instructor
Quiet Fern Yoga
Creative Brief
Use same font as used in my logo
Use fonts that you feel work well with the logo and style of card
Bright & Fun-filled
Miriam Tovbrask
Certified Yoga Instructor
Larkmoor, Vestal
mtovbrask@brightpost.example
www.Quietfern.example
The front should include the "Quiett Fern Yoga" logo that we have uploaded. Also - we would like to include "Offering Veyolin based yoga" on the card as well. perhaps just below the title "Certified Yoga Instructor"
we would like to have the "Ohm" symbol on the back of the card and the words "Strength - Stability - Freedom". here is a link for a sample of the symbol. http://www.breathwheelsite.example/ok.htm We are thinking the Ohm symbol can fill the entire back (even going off the edges) and the text on top.

```html
<!DOCTYPE html>
<html lang="en">
<head>
<meta charset="utf-8">
<title>Quiet Fern Yoga – Business cards</title>
<link rel="stylesheet" href="https://fonts.googleapis.com/css2?family=PT+Sans:ital,wght@0,400;0,700;1,400;1,700&family=PT+Sans+Narrow:wght@400;700&display=swap">
<style>
  :root {
    --board: #a4a09f;
    --board-text: #ffffff;
    --ink: #1c1c1c;
    --name-purple: #5a3a8c;
    --accent-pink: #c0479a;
    --logo-pink: #c85aa6;
    --rule: #8a6fb0;
    --card-white: #ffffff;
    --card-tint: #c9d8de;
    --back-deep: #7fa3b1;
    --back-light: #bccfd6;
    --back-mark: #a9c1ca;
    --swatch-black: #161616;
    --badge: #8f8b8a;
  }
  * { margin: 0; padding: 0; box-sizing: border-box; }
  html, body { width: 1200px; height: 888px; overflow: hidden; }
  body {
    background: var(--board);
    font-family: "PT Sans", sans-serif;
    color: var(--board-text);
    position: relative;
  }
  .sheet-header { position: absolute; left: 91px; top: 14px; }
  .sheet-title { font: italic 700 27px/1.1 "PT Sans", sans-serif; }
  .sheet-subtitle { font: italic 400 19px/1.2 "PT Sans", sans-serif; margin-top: 2px; }
  .sheet-note { font: 400 14px/1.3 "PT Sans Narrow", sans-serif; margin-top: 6px; }

  .variant-label {
    position: absolute;
    display: flex; align-items: center; gap: 8px;
    font: 400 13px/1 "PT Sans Narrow", sans-serif;
  }
  .variant-badge {
    width: 24px; height: 24px; border-radius: 50%;
    background: var(--badge); color: var(--board-text);
    font: 700 11px/24px "PT Sans", sans-serif; text-align: center;
  }

  .card {
    position: absolute;
    width: 480px; height: 274px;
    border-radius: 10px;
    overflow: hidden;
    box-shadow: 0 3px 8px rgba(0,0,0,0.25);
  }
  .card-front {
    background:
      radial-gradient(ellipse 55% 55% at 0% 100%, var(--card-tint), transparent 70%),
      radial-gradient(ellipse 50% 60% at 100% 100%, var(--card-tint), transparent 70%),
      radial-gradient(ellipse 40% 35% at 100% 0%, #e3ebee, transparent 70%),
      var(--card-white);
  }
  .brand {
    position: absolute; top: 68px;
    display: flex; align-items: center; gap: 10px;
    font: 400 32px/1 "PT Sans", sans-serif;
    color: var(--logo-pink);
    white-space: nowrap;
  }
  .brand-dot { width: 18px; height: 18px; border-radius: 50%; background: var(--logo-pink); }
  .brand-left { left: 36px; }
  .brand-right { left: 56px; }

  .holder { position: absolute; left: 36px; top: 156px; color: var(--ink); white-space: nowrap; }
  .holder-name { font: 400 20px/1.1 "PT Sans", sans-serif; color: var(--name-purple); }
  .holder-title { font: 400 12px/1.4 "PT Sans", sans-serif; margin-top: 3px; }
  .holder-offer { font: italic 400 12px/1.4 "PT Sans", sans-serif; color: var(--accent-pink); margin-top: 8px; }

  .divider { position: absolute; left: 271px; top: 148px; width: 1px; height: 86px; background: var(--rule); }
  .contact {
    position: absolute; left: 290px; top: 158px;
    list-style: none; color: var(--ink);
    font: 400 10.5px/18.5px "PT Sans", sans-serif;
    white-space: nowrap;
  }

  .card-back {
    width: 480px; height: 274px;
    left: 112px; top: 548px;
    transform: rotate(-5deg);
    background: linear-gradient(135deg, var(--back-light) 0%, var(--back-deep) 65%, #93b2be 100%);
  }
  .back-mark {
    position: absolute; left: -40px; top: -60px;
    width: 520px; height: 420px; border-radius: 50%;
    background: radial-gradient(ellipse at 45% 45%, var(--back-mark) 0%, rgba(169,193,202,0.35) 55%, transparent 75%);
  }
  .back-motto {
    position: absolute; left: 34px; top: 136px;
    font: italic 400 22px/1 "PT Sans", sans-serif;
    color: var(--board-text);
    letter-spacing: 0.5px;
    white-space: nowrap;
  }

  .palette { position: absolute; left: 689px; top: 556px; white-space: nowrap; }
  .palette-title { font: italic 700 19px/1 "PT Sans", sans-serif; margin-bottom: 12px; }
  .palette-row { position: relative; font: 400 14px/1 "PT Sans Narrow", sans-serif; height: 19px; }
  .palette-row .value { position: absolute; left: 199px; top: 0; white-space: nowrap; }
  .swatch { position: absolute; left: 156px; top: -6px; width: 34px; height: 26px; border: 1px solid #ffffff; }
  .swatch-black { background: var(--swatch-black); }
  .swatch-base { background: linear-gradient(135deg, var(--back-light), var(--back-deep)); }
</style>
</head>
<body>
  <header class="sheet-header">
    <h1 class="sheet-title">Miriam Tovbrask</h1>
    <p class="sheet-subtitle">Yoga Instructor - Business cards</p>
    <p class="sheet-note">The same designs as draft #58, with some changes and the color scheme of #36, 13a and 18.</p>
  </header>

  <div class="variant-label" style="left:108px; top:152px;"><span class="variant-badge">15a</span>Left placement of the logo.</div>
  <div class="variant-label" style="left:629px; top:152px;"><span class="variant-badge">15b</span>Right placement of the logo.</div>
  <div class="variant-label" style="left:108px; top:500px;"><span class="variant-badge">15c</span></div>

  <article class="card card-front" style="left:108px; top:187px;">
    <div class="brand brand-left">Quiet Fern Yoga<span class="brand-dot"></span></div>
    <div class="holder">
      <p class="holder-name">Miriam Tovbrask</p>
      <p class="holder-title">Certified Yoga Instructor</p>
      <p class="holder-offer">Offering Veyolin based yoga</p>
    </div>
    <div class="divider"></div>
    <ul class="contact">
      <li>Larkmoor, Vestal</li>
      <li>(555) 550-0148</li>
      <li>mtovbrask@brightpost.example</li>
      <li>www.Quietfern.example</li>
    </ul>
  </article>

  <article class="card card-front" style="left:629px; top:187px;">
    <div class="brand brand-right">Quiet Fern Yoga<span class="brand-dot"></span></div>
    <div class="holder">
      <p class="holder-name">Miriam Tovbrask</p>
      <p class="holder-title">Certified Yoga Instructor</p>
      <p class="holder-offer">Offering Veyolin based yoga</p>
    </div>
    <div class="divider"></div>
    <ul class="contact">
      <li>Larkmoor, Vestal</li>
      <li>(555) 550-0148</li>
      <li>mtovbrask@brightpost.example</li>
      <li>www.Quietfern.example</li>
    </ul>
  </article>

  <article class="card card-back">
    <div class="back-mark" role="img" aria-label="Large faint Om symbol filling the back of the card"></div>
    <p class="back-motto">Strength • Stability • Freedom</p>
  </article>

  <section class="palette">
    <h2 class="palette-title">Colors</h2>
    <div class="palette-row">Quiet Fern logo colors</div>
    <div class="palette-row">+</div>
    <div class="palette-row">For text:<span class="swatch swatch-black"></span><span class="value">Black 100%</span></div>
    <div class="palette-row">+</div>
    <div class="palette-row">Base gradient color:<span class="swatch swatch-base"></span><span class="value">C: 64 &nbsp;M: 28 &nbsp;Y: 28 &nbsp;K: 0</span></div>
  </section>
</body>
</html>
```